Digital marketing agency needs a new website design

We need a new responsive design for our website: https://brivolta.com/

Brivolta is a french digital marketing company who specializes in helping companies rank higher on Quendo search engine for their keywords in order to be more visible and have more traffic and clients.

I need you to design these 5 pages:
- Home page: https://brivolta.com
- Pricing page: https://brivolta.com/packs-backlinks/
- Contact page: https://brivolta.com/contact/
- Thank you page: https://brivolta.com/merci-temp/
- Simple page : https://brivolta.com/a-propos/

Here is a list of websites that we like their design. Use it for inspiration, but make sure it is different :

https://fenrolt.io/ (this is the one I like the most)
https://ubro.com/
http://www.garvelnest.com/
https://lumbardeau.fr/
https://www.tressaplank.com/home
https://dovermick.com/fr/
https://kalvoxa.io/
https://tramoisenet.fr/

I want a 75% color background and 25% white. You should use many bright/pastel colors like this website : https://fenrolt.io/

Keep the contact form in the website header.

Target Market(s)

small business owners

Industry/Entity Type

Digital Marketing

Number of Pages Required

5+ page

Font styles to use
Sans Serif

Colors

Designer to choose colors to be used in the design.

Requirements
Must have
• Contact form in header.
• Prominent call-to-action buttons.
• Use of at least 1 flashy color, possible to use many.
• Keep the 3 chart images.
• Keep client testimonials

```html
<!DOCTYPE html>
<html lang="fr">
<head>
<meta charset="utf-8">
<title>Brivolta – Résultats obtenus avec nos backlinks</title>
<link rel="stylesheet" href="https://fonts.googleapis.com/css2?family=Exo+2:wght@300;400;800&family=Roboto:wght@400;500&display=swap">
<style>
  :root {
    --bg-start: #3a56ea;
    --bg-end: #8a4ff6;
    --white: #ffffff;
    --chrome-dark: #202124;
    --chrome-bar: #35363a;
    --chrome-tab: #4a4b4f;
    --ga-line: #058dc7;
    --ga-fill: #e5f1f8;
    --ga-grid: #e6e6e6;
    --ga-text: #333333;
    --ga-link: #1a5fb4;
    --ga-border: #cccccc;
    --ga-btn: #f4f4f4;
    --ga-btn-on: #dcdcdc;
  }
  * { margin: 0; padding: 0; box-sizing: border-box; }
  html, body { width: 1200px; height: 1200px; overflow: hidden; }
  body {
    position: relative;
    background: linear-gradient(160deg, var(--bg-start) 0%, #5a4ff0 50%, var(--bg-end) 100%);
    font-family: "Exo 2", sans-serif;
    color: var(--white);
  }
  .bottom-wave { position: absolute; left: 0; top: 0; width: 1200px; height: 1200px; }
  .page-title {
    position: absolute; left: 0; top: 16px; width: 1200px;
    text-align: center; font-weight: 800; font-size: 43px; line-height: 48px;
    letter-spacing: 2px;
  }
  .result-copy { position: absolute; }
  .result-copy h2 {
    font-weight: 800; font-size: 33px; line-height: 38px; letter-spacing: 1.5px;
  }
  .result-copy p {
    margin-top: 10px; font-weight: 300; font-size: 19.5px; line-height: 25px; letter-spacing: 1.2px;
  }
  .copy-one { left: 680px; top: 258px; }
  .copy-two { left: 231px; top: 571px; }
  .copy-three { left: 681px; top: 907px; }
  .analytics-shot {
    position: absolute; width: 404px; height: 227px;
    box-shadow: 0 6px 18px rgba(20, 10, 80, 0.25);
  }
  .shot-one { left: 173px; top: 194px; }
  .shot-two { left: 622px; top: 526px; }
  .shot-three { left: 170px; top: 858px; }
  .ga { font-family: "Roboto", Arial, sans-serif; }
  .ga-small { font-size: 8.5px; fill: var(--ga-text); }
  .ga-link { font-size: 8.5px; fill: var(--ga-link); }
  .ga-tiny { font-size: 7px; fill: var(--ga-text); }
  .ga-bold { font-size: 9px; font-weight: 500; fill: var(--ga-text); }
  .ga-chrome { font-size: 5px; fill: #c8c8c8; }
</style>
</head>
<body>

<svg class="bottom-wave" viewBox="0 0 1200 1200" aria-hidden="true">
  <path d="M0 1022 C180 975 420 960 585 1052 C705 1122 800 1186 885 1190 C1000 1196 1120 1132 1200 1086 L1200 1200 L0 1200 Z" fill="var(--white)"/>
</svg>

<h1 class="page-title">Exemples de Résultats Obtenus<br>Avec Nos Backlinks</h1>

<!-- Result 1 -->
<svg class="analytics-shot shot-one ga" viewBox="0 0 505 284" role="img" aria-label="Graphique des sessions mensuelles, d'avril 2017 à juillet 2018">
  <rect width="505" height="284" fill="var(--white)"/>
  <rect width="505" height="32" fill="var(--chrome-dark)"/>
  <rect x="0" y="16" width="505" height="16" fill="var(--chrome-bar)"/>
  <rect x="30" y="3" width="95" height="13" rx="3" fill="var(--chrome-tab)"/>
  <circle cx="7" cy="9" r="2.2" fill="#ff5f57"/><circle cx="14" cy="9" r="2.2" fill="#febc2e"/><circle cx="21" cy="9" r="2.2" fill="#28c840"/>
  <circle cx="39" cy="10" r="2.5" fill="#f6c026"/>
  <text x="45" y="12" class="ga-chrome">Brivolta</text>
  <text x="117" y="12" class="ga-chrome">×</text><text x="131" y="12" class="ga-chrome">+</text>
  <text x="6" y="27" class="ga-chrome">←  →  C</text>
  <text x="48" y="27" class="ga-chrome">🔒 https://brivolta.com</text>
  <rect x="2" y="37" width="48" height="25" fill="var(--white)" stroke="var(--ga-border)"/>
  <text x="8" y="54" class="ga-bold">Explorer</text>
  <line x1="50" y1="61" x2="505" y2="61" stroke="var(--ga-border)"/>
  <text x="7" y="79" class="ga-small">Summary</text>
  <text x="60" y="79" class="ga-link">Site Usage</text>
  <text x="117" y="79" class="ga-link">Ecommerce</text>
  <text x="180" y="79" class="ga-link">Ad Revenue</text>
  <line x1="0" y1="88" x2="505" y2="88" stroke="var(--ga-grid)"/>
  <rect x="9" y="96" width="55" height="23" fill="var(--white)" stroke="var(--ga-border)"/>
  <text x="14" y="111" class="ga-tiny">Sessions  ▾</text>
  <text x="69" y="111" class="ga-tiny">VS.</text>
  <text x="89" y="111" class="ga-tiny" fill="var(--ga-link)">Select a metric</text>
  <rect x="365" y="97" width="90" height="22" fill="var(--ga-btn)" stroke="var(--ga-border)"/>
  <rect x="421" y="97" width="34" height="22" fill="var(--ga-btn-on)"/>
  <text x="370" y="111" class="ga-tiny">Day</text><text x="395" y="111" class="ga-tiny">Week</text><text x="426" y="111" class="ga-tiny">Month</text>
  <rect x="463" y="97" width="22" height="22" fill="var(--ga-btn-on)" stroke="var(--ga-border)"/>
  <rect x="485" y="97" width="20" height="22" fill="var(--ga-btn)" stroke="var(--ga-border)"/>
  <path d="M468 113 L473 108 L477 111 L481 105" stroke="#333" fill="none"/>
  <circle cx="492" cy="106" r="2" fill="#333"/><circle cx="497" cy="111" r="2" fill="#333"/><circle cx="491" cy="112" r="1.6" fill="#333"/>
  <circle cx="12" cy="138" r="4" fill="var(--ga-line)"/>
  <text x="22" y="141" class="ga-small">Sessions</text>
  <text x="16" y="160" class="ga-tiny">30,000</text>
  <text x="16" y="210" class="ga-tiny">15,000</text>
  <line x1="14" y1="163" x2="491" y2="163" stroke="var(--ga-grid)"/>
  <line x1="14" y1="213" x2="491" y2="213" stroke="var(--ga-grid)"/>
  <path d="M14 250 L42 250 L71 249 L99 248 L127 245 L155 212 L183 191 L211 203 L239 209 L267 209 L295 212 L323 213 L351 216 L379 213 L407 210 L435 207 L463 184 L491 163 L491 251 L14 251 Z" fill="var(--ga-fill)"/>
  <polyline points="14,250 42,250 71,249 99,248 127,245 155,212 183,191 211,203 239,209 267,209 295,212 323,213 351,216 379,213 407,210 435,207 463,184 491,163" fill="none" stroke="var(--ga-line)" stroke-width="2"/>
  <g fill="var(--ga-line)">
    <circle cx="14" cy="250" r="3"/><circle cx="42" cy="250" r="3"/><circle cx="71" cy="249" r="3"/><circle cx="99" cy="248" r="3"/><circle cx="127" cy="245" r="3"/><circle cx="155" cy="212" r="3"/><circle cx="183" cy="191" r="3"/><circle cx="211" cy="203" r="3"/><circle cx="239" cy="209" r="3"/><circle cx="267" cy="209" r="3"/><circle cx="295" cy="212" r="3"/><circle cx="323" cy="213" r="3"/><circle cx="351" cy="216" r="3"/><circle cx="379" cy="213" r="3"/><circle cx="407" cy="210" r="3"/><circle cx="435" cy="207" r="3"/><circle cx="463" cy="184" r="3"/><circle cx="491" cy="163" r="3"/>
  </g>
  <line x1="12" y1="251" x2="493" y2="251" stroke="#555"/>
  <text x="23" y="262" class="ga-tiny">April 2017</text>
  <text x="107" y="262" class="ga-tiny">July 2017</text>
  <text x="185" y="262" class="ga-tiny">October 2017</text>
  <text x="270" y="262" class="ga-tiny">January 2018</text>
  <text x="358" y="262" class="ga-tiny">April 2018</text>
  <text x="443" y="262" class="ga-tiny">July 2018</text>
</svg>

<div class="result-copy copy-one">
  <h2>De 0 à 26 000<br>visites/mois</h2>
  <p>Et ça continue d’augmenter!</p>
</div>

<!-- Result 2 -->
<svg class="analytics-shot shot-two ga" viewBox="0 0 505 284" role="img" aria-label="Graphique des sessions mensuelles, de juin 2017 à juin 2018">
  <rect width="505" height="284" fill="var(--white)"/>
  <rect width="505" height="32" fill="var(--chrome-dark)"/>
  <rect x="0" y="16" width="505" height="16" fill="var(--chrome-bar)"/>
  <rect x="30" y="3" width="95" height="13" rx="3" fill="var(--chrome-tab)"/>
  <circle cx="7" cy="9" r="2.2" fill="#ff5f57"/><circle cx="14" cy="9" r="2.2" fill="#febc2e"/><circle cx="21" cy="9" r="2.2" fill="#28c840"/>
  <circle cx="39" cy="10" r="2.5" fill="#f6c026"/>
  <text x="45" y="12" class="ga-chrome">Brivolta</text>
  <text x="117" y="12" class="ga-chrome">×</text><text x="131" y="12" class="ga-chrome">+</text>
  <text x="6" y="27" class="ga-chrome">←  →  C</text>
  <text x="48" y="27" class="ga-chrome">🔒 https://brivolta.com</text>
  <rect x="2" y="37" width="48" height="25" fill="var(--white)" stroke="var(--ga-border)"/>
  <text x="8" y="54" class="ga-bold">Explorer</text>
  <line x1="50" y1="61" x2="505" y2="61" stroke="var(--ga-border)"/>
  <text x="8" y="79" class="ga-small">Summary</text>
  <text x="60" y="79" class="ga-link">Site Usage</text>
  <text x="118" y="79" class="ga-link">Goal Set 1</text>
  <text x="173" y="79" class="ga-link">Goal Set 2</text>
  <text x="229" y="79" class="ga-link">Goal Set 3</text>
  <text x="284" y="79" class="ga-link">Ecommerce</text>
  <line x1="0" y1="88" x2="505" y2="88" stroke="var(--ga-grid)"/>
  <rect x="9" y="97" width="55" height="23" fill="var(--white)" stroke="var(--ga-border)"/>
  <text x="14" y="112" class="ga-tiny">Sessions  ▾</text>
  <text x="69" y="112" class="ga-tiny">VS.</text>
  <text x="89" y="112" class="ga-tiny" fill="var(--ga-link)">Select a metric</text>
  <rect x="365" y="98" width="90" height="22" fill="var(--ga-btn)" stroke="var(--ga-border)"/>
  <rect x="421" y="98" width="34" height="22" fill="var(--ga-btn-on)"/>
  <text x="370" y="112" class="ga-tiny">Day</text><text x="395" y="112" class="ga-tiny">Week</text><text x="426" y="112" class="ga-tiny">Month</text>
  <rect x="463" y="98" width="22" height="22" fill="var(--ga-btn-on)" stroke="var(--ga-border)"/>
  <rect x="485" y="98" width="20" height="22" fill="var(--ga-btn)" stroke="var(--ga-border)"/>
  <path d="M468 114 L473 109 L477 112 L481 106" stroke="#333" fill="none"/>
  <circle cx="492" cy="107" r="2" fill="#333"/><circle cx="497" cy="112" r="2" fill="#333"/><circle cx="491" cy="113" r="1.6" fill="#333"/>
  <circle cx="12" cy="138" r="4" fill="var(--ga-line)"/>
  <text x="22" y="142" class="ga-small">Sessions</text>
  <text x="16" y="160" class="ga-tiny">5,000</text>
  <text x="16" y="210" class="ga-tiny">2,500</text>
  <line x1="14" y1="163" x2="492" y2="163" stroke="var(--ga-grid)"/>
  <line x1="14" y1="213" x2="492" y2="213" stroke="var(--ga-grid)"/>
  <path d="M14 228 L54 227 L94 227 L134 222 L175 188 L215 186 L255 185 L295 183 L335 154 L375 181 L412 171 L452 174 L492 163 L492 252 L14 252 Z" fill="var(--ga-fill)"/>
  <polyline points="14,228 54,227 94,227 134,222 175,188 215,186 255,185 295,183 335,154 375,181 412,171 452,174 492,163" fill="none" stroke="var(--ga-line)" stroke-width="2"/>
  <g fill="var(--ga-line)">
    <circle cx="14" cy="228" r="3"/><circle cx="54" cy="227" r="3"/><circle cx="94" cy="227" r="3"/><circle cx="134" cy="222" r="3"/><circle cx="175" cy="188" r="3"/><circle cx="215" cy="186" r="3"/><circle cx="255" cy="185" r="3"/><circle cx="295" cy="183" r="3"/><circle cx="335" cy="154" r="3"/><circle cx="375" cy="181" r="3"/><circle cx="412" cy="171" r="3"/><circle cx="452" cy="174" r="3"/><circle cx="492" cy="163" r="3"/>
  </g>
  <line x1="12" y1="252" x2="494" y2="252" stroke="#555"/>
  <text x="77" y="262" class="ga-tiny">July 2017</text>
  <text x="190" y="262" class="ga-tiny">October 2017</text>
  <text x="310" y="262" class="ga-tiny">January 2018</text>
  <text x="434" y="262" class="ga-tiny">April 2018</text>
</svg>

<div class="result-copy copy-two">
  <h2>De 1 200 à 4 400<br>visites/mois</h2>
  <p>Le trafic en provenance de Quendo<br>a plus que triplé en 12 mois.</p>
</div>

<!-- Result 3 -->
<svg class="analytics-shot shot-three ga" viewBox="0 0 505 284" role="img" aria-label="Graphique des sessions hebdomadaires, de juillet 2017 à juillet 2018">
  <rect width="505" height="284" fill="var(--white)"/>
  <rect width="505" height="32" fill="var(--chrome-dark)"/>
  <rect x="0" y="16" width="505" height="16" fill="var(--chrome-bar)"/>
  <rect x="30" y="3" width="95" height="13" rx="3" fill="var(--chrome-tab)"/>
  <circle cx="7" cy="9" r="2.2" fill="#ff5f57"/><circle cx="14" cy="9" r="2.2" fill="#febc2e"/><circle cx="21" cy="9" r="2.2" fill="#28c840"/>
  <circle cx="39" cy="10" r="2.5" fill="#f6c026"/>
  <text x="45" y="12" class="ga-chrome">Brivolta</text>
  <text x="117" y="12" class="ga-chrome">×</text><text x="131" y="12" class="ga-chrome">+</text>
  <text x="6" y="27" class="ga-chrome">←  →  C</text>
  <text x="48" y="27" class="ga-chrome">🔒 https://brivolta.com</text>
  <rect x="2" y="38" width="50" height="24" fill="var(--white)" stroke="var(--ga-border)"/>
  <text x="9" y="54" class="ga-bold">Explorer</text>
  <line x1="52" y1="61" x2="505" y2="61" stroke="var(--ga-border)"/>
  <text x="8" y="78" class="ga-small">Summary</text>
  <text x="60" y="78" class="ga-link">Site Usage</text>
  <text x="117" y="78" class="ga-link">Ecommerce</text>
  <text x="180" y="78" class="ga-link">Ad Revenue</text>
  <line x1="0" y1="88" x2="505" y2="88" stroke="var(--ga-grid)"/>
  <rect x="10" y="96" width="56" height="23" fill="var(--white)" stroke="var(--ga-border)"/>
  <text x="16" y="111" class="ga-tiny">Sessions  ▾</text>
  <text x="70" y="111" class="ga-tiny">VS.</text>
  <text x="90" y="111" class="ga-tiny" fill="var(--ga-link)">Select a metric</text>
  <rect x="366" y="97" width="86" height="22" fill="var(--ga-btn)" stroke="var(--ga-border)"/>
  <rect x="391" y="97" width="31" height="22" fill="var(--ga-btn-on)"/>
  <text x="371" y="111" class="ga-tiny">Day</text><text x="396" y="111" class="ga-tiny">Week</text><text x="427" y="111" class="ga-tiny">Month</text>
  <rect x="463" y="97" width="22" height="22" fill="var(--ga-btn-on)" stroke="var(--ga-border)"/>
  <rect x="485" y="97" width="20" height="22" fill="var(--ga-btn)" stroke="var(--ga-border)"/>
  <path d="M468 113 L473 108 L477 111 L481 105" stroke="#333" fill="none"/>
  <circle cx="492" cy="106" r="2" fill="#333"/><circle cx="497" cy="111" r="2" fill="#333"/><circle cx="491" cy="112" r="1.6" fill="#333"/>
  <circle cx="14" cy="136" r="4" fill="var(--ga-line)"/>
  <text x="24" y="140" class="ga-small">Sessions</text>
  <text x="13" y="156" class="ga-tiny">100,000</text>
  <text x="13" y="207" class="ga-tiny">50,000</text>
  <line x1="10" y1="146" x2="491" y2="146" stroke="var(--ga-grid)"/>
  <line x1="10" y1="197" x2="491" y2="197" stroke="var(--ga-grid)"/>
  <path d="M10 248 L118 248 L126 246 L134 238 L142 229 L150 222 L158 217 L166 215 L174 214 L182 212 L190 211 L198 212 L206 209 L214 200 L222 202 L230 196 L238 178 L246 192 L254 200 L262 197 L270 207 L278 202 L286 196 L294 200 L302 194 L310 206 L318 199 L326 209 L334 207 L342 211 L350 213 L358 216 L366 214 L374 219 L382 212 L390 216 L398 209 L406 205 L414 202 L422 201 L430 195 L438 190 L446 203 L454 203 L462 194 L470 188 L478 191 L486 194 L491 191 L491 248 Z" fill="var(--ga-fill)"/>
  <path d="M10 248 L118 248 L126 246 L134 238 L142 229 L150 222 L158 217 L166 215 L174 214 L182 212 L190 211 L198 212 L206 209 L214 200 L222 202 L230 196 L238 178 L246 192 L254 200 L262 197 L270 207 L278 202 L286 196 L294 200 L302 194 L310 206 L318 199 L326 209 L334 207 L342 211 L350 213 L358 216 L366 214 L374 219 L382 212 L390 216 L398 209 L406 205 L414 202 L422 201 L430 195 L438 190 L446 203 L454 203 L462 194 L470 188 L478 191 L486 194 L491 191" fill="none" stroke="var(--ga-line)" stroke-width="1.6"/>
  <line x1="10" y1="248" x2="491" y2="248" stroke="#555"/>
  <text x="41" y="258" class="ga-tiny">July 2017</text>
  <text x="130" y="258" class="ga-tiny">October 2017</text>
  <text x="228" y="258" class="ga-tiny">January 2018</text>
  <text x="328" y="258" class="ga-tiny">April 2018</text>
  <text x="426" y="258" class="ga-tiny">July 2018</text>
</svg>

<div class="result-copy copy-three">
  <h2>De 0 à 60 000<br>visites/semaine</h2>
  <p>C’est plus de 240 000 visites<br>par mois pour ce site.</p>
</div>

</body>
</html>
```